FotoVELTA buisnesscard

Hey :) I need a modern buisnesscard for my company FotoVELTA
It most have:
Dagligleder og Fotograf: Henrik Torvald Bjelland

Mob: +4791642058
Epost: post@fotovelta.no
Adresse: Bakkestien22, 6030 Langevåg

Facbook and instagram logo with text FotoVELTA

FotoVELTA logo

It Company

```html
<!DOCTYPE html>
<html lang="no">
<head>
<meta charset="utf-8">
<title>FotoVELTA – visittkort</title>
<link href="https://fonts.googleapis.com/css2?family=Roboto:ital,wght@0,400;0,700;1,400;1,700&display=swap" rel="stylesheet">
<style>
  :root {
    --backdrop: #121212;
    --card: #262626;
    --card-edge: #303030;
    --text-light: #d9d9d9;
    --text-muted: #9a9a9a;
    --divider: #7a7a7a;
    --brand-blue: #1f8fbf;
    --brand-pink: #d93f8c;
  }
  * { margin: 0; padding: 0; box-sizing: border-box; }
  html, body { width: 1200px; height: 890px; overflow: hidden; }
  body {
    background: var(--backdrop);
    font-family: "Roboto", Arial, sans-serif;
    display: flex;
    align-items: center;
    justify-content: center;
    gap: 40px;
  }
  .card {
    width: 540px;
    height: 340px;
    background: var(--card);
    border: 1px solid var(--card-edge);
    border-radius: 4px;
    position: relative;
  }

  /* Contact side */
  .card--contact {
    display: flex;
    align-items: center;
    justify-content: center;
    gap: 16px;
  }
  .person { text-align: right; }
  .person__name {
    font-weight: 700;
    font-style: italic;
    font-size: 15px;
    letter-spacing: 0.2px;
    text-transform: uppercase;
    color: var(--text-light);
  }
  .person__role {
    font-style: italic;
    font-size: 13px;
    color: var(--text-muted);
    margin-top: 3px;
  }
  .divider {
    width: 1px;
    height: 52px;
    background: var(--divider);
  }
  .contact-list { list-style: none; }
  .contact-list li {
    display: flex;
    align-items: center;
    gap: 7px;
    font-style: italic;
    font-size: 13px;
    line-height: 18px;
    color: var(--text-light);
  }
  .contact-list svg { width: 12px; height: 12px; flex: none; }

  /* Brand side */
  .card--brand {
    display: flex;
    flex-direction: column;
    align-items: center;
    justify-content: center;
    gap: 34px;
  }
  .brand {
    display: flex;
    align-items: center;
    gap: 14px;
  }
  .brand__square {
    width: 30px;
    height: 30px;
    background: var(--brand-pink);
  }
  .brand__name {
    font-weight: 700;
    font-size: 46px;
    color: var(--brand-blue);
  }
  .social {
    display: flex;
    align-items: center;
    gap: 12px;
  }
  .social__link {
    width: 24px;
    height: 24px;
    border-radius: 4px;
  }
  .social__link--facebook { background: var(--brand-blue); }
  .social__link--instagram { background: var(--brand-pink); }
</style>
</head>
<body>
  <section class="card card--contact" aria-label="Kontaktside">
    <div class="person">
      <p class="person__name">Henrik Torvald Bjelland</p>
      <p class="person__role">Dagligleder og Fotograf</p>
    </div>
    <span class="divider"></span>
    <ul class="contact-list">
      <li>
        <svg viewBox="0 0 12 12" aria-hidden="true"><rect x="3" y="0.8" width="6" height="10.4" rx="1.2" fill="none" stroke="#d9d9d9" stroke-width="1.2"/><circle cx="6" cy="9.3" r="0.7" fill="#d9d9d9"/></svg>
        +4791642058
      </li>
      <li>
        <svg viewBox="0 0 12 12" aria-hidden="true"><rect x="0.8" y="2.5" width="10.4" height="7" fill="none" stroke="#d9d9d9" stroke-width="1.2"/><path d="M1 3 L6 7 L11 3" fill="none" stroke="#d9d9d9" stroke-width="1.2"/></svg>
        post@fotovelta.no
      </li>
      <li>
        <svg viewBox="0 0 12 12" aria-hidden="true"><path d="M6 11.4 C3 7.6 2.4 6.2 2.4 4.6 A3.6 3.6 0 0 1 9.6 4.6 C9.6 6.2 9 7.6 6 11.4 Z" fill="none" stroke="#d9d9d9" stroke-width="1.2"/><circle cx="6" cy="4.6" r="1.2" fill="#d9d9d9"/></svg>
        Bakkestien22, 6030 Langevåg
      </li>
    </ul>
  </section>

  <section class="card card--brand" aria-label="Logoside">
    <div class="brand">
      <span class="brand__square"></span>
      <span class="brand__name">FotoVELTA</span>
    </div>
    <div class="social">
      <span class="social__link social__link--facebook" role="img" aria-label="Facebook-profil for FotoVELTA"></span>
      <span class="social__link social__link--instagram" role="img" aria-label="Instagram-profil for FotoVELTA"></span>
    </div>
  </section>
</body>
</html>
```